Flyer for annual KESTREL SUMMIT 2020

I would like a church event flyer designed. The event is called "KESTREL SUMMIT 2020". I am looking for a professional, yet catchy design that uses our brand colors and logo creatively while communicating key information of the event effectively.

1. The logo is attached in two color formats. The designer has the choice to use them as he/she want.

2. The location of the event is: Harlow Community Center, 239 Fennimore Street, Portland, ME 04117

3. Time and date of event. The designer can organize and format the date and time as he/she pleases.
Thursday December 31st @ 6:30PM
Friday January 1st @ 6:30PM
Saturday 2nd @ 6:30PM
Sunday 3rd @ 4:30PM

4. The topic of the event is "In Fire and On Fire". The designer is free to use this phrase as he/she pleases to create a good composition.

5. Speaker: Prophet Marcus Olunde (2 pictures of the speaker to choose from are attached)

6. Contact information: contact@brightmeadowfold.org - Telephone number: 207 583 2914

7. I would also like the following three words on the flyer. These words describe the focus of the event: FIRE, REVIVAL, PROPHETIC

Target Market(s)

Young adults

Font styles to use
Sans Serif

Requirements
Must have
• Logo, speaker's picture
Should not have
• cross image, church image

```html
<!DOCTYPE html>
<html lang="en">
<head>
<meta charset="utf-8">
<title>Kestrel Summit 2020</title>
<link rel="stylesheet" href="https://fonts.googleapis.com/css2?family=Anton&family=Great+Vibes&family=Cormorant+Garamond:wght@500&family=Libre+Baskerville:ital@0;1&display=swap">
<style>
  :root {
    --navy: #15355b;
    --orange: #ef8e2a;
    --red: #c8202a;
    --red-dark: #a5161f;
    --peach: #f5a887;
    --peach-soft: #fbd8c6;
    --paper: #ffffff;
    --card: #f4f4f4;
    --card-edge: #c9c9c9;
    --photo-warm: #ee7a4a;
    --photo-light: #f8c2a6;
  }
  * { margin: 0; padding: 0; box-sizing: border-box; }
  html, body { width: 927px; height: 1200px; overflow: hidden; }
  body {
    position: relative;
    background:
      radial-gradient(ellipse 420px 300px at 15% 5%, rgba(240,120,80,.55), transparent 70%),
      radial-gradient(ellipse 380px 260px at 80% 3%, rgba(245,150,120,.45), transparent 70%),
      radial-gradient(ellipse 520px 240px at 50% 33%, #ffffff 30%, transparent 75%),
      radial-gradient(ellipse 600px 200px at 40% 55%, #ffffff 35%, transparent 80%),
      radial-gradient(ellipse 560px 260px at 20% 92%, rgba(240,125,90,.55), transparent 70%),
      radial-gradient(ellipse 560px 280px at 85% 95%, rgba(242,130,100,.5), transparent 70%),
      linear-gradient(180deg, var(--peach-soft) 0%, #fff4ee 35%, #ffffff 55%, var(--peach-soft) 78%, var(--peach) 100%);
    font-family: "Libre Baskerville", serif;
    color: var(--navy);
  }
  .abs { position: absolute; }

  .event-title {
    left: 46px; top: 60px;
    font-family: "Anton", sans-serif;
    font-size: 132px; line-height: 1;
    letter-spacing: -2px;
    color: var(--navy);
  }
  .event-subtitle {
    left: 200px; top: 150px;
    font-family: "Great Vibes", cursive;
    font-size: 108px; line-height: 1;
    color: var(--orange);
  }
  .event-year {
    left: 423px; top: 230px;
    font-family: "Anton", sans-serif;
    font-size: 44px; line-height: 1;
    color: var(--orange);
  }
  .dove { border-radius: 50%; background: radial-gradient(circle, #ffffff 35%, rgba(236,230,226,.8) 55%, rgba(255,255,255,0) 72%); }
  .dove-top { left: 470px; top: 58px; width: 115px; height: 128px; }
  .dove-mid { left: 400px; top: 530px; width: 124px; height: 108px; }

  .brand { left: 640px; top: 78px; display: flex; align-items: center; gap: 10px; }
  .brand-dot { width: 14px; height: 14px; border-radius: 50%; background: var(--orange); }
  .brand-name {
    font-family: "Cormorant Garamond", serif; font-weight: 500;
    font-size: 64px; line-height: 1; color: var(--navy); letter-spacing: 1px;
  }

  .speaker-photo {
    left: 604px; top: 203px; width: 313px; height: 480px;
    border-radius: 6px;
    background: linear-gradient(180deg, var(--photo-light) 0%, var(--photo-warm) 55%, var(--photo-light) 100%);
  }

  .theme { left: 48px; top: 345px; font-family: "Libre Baskerville", serif; font-style: italic; color: var(--navy); }
  .theme-line { display: block; font-size: 60px; line-height: 1; letter-spacing: -1px; }
  .theme-line-2 { margin-left: 176px; margin-top: -6px; }
  .theme-amp {
    left: 295px; top: 330px;
    font-family: "Great Vibes", cursive; font-size: 110px; line-height: 1; color: var(--orange);
  }

  .focus-words {
    left: 48px; top: 488px;
    font-size: 17px; letter-spacing: 5.2px; color: var(--navy);
    white-space: nowrap;
  }

  .speaker {
    left: 48px; top: 657px;
    font-family: "Anton", sans-serif; font-size: 29px; line-height: 1;
    color: var(--navy);
  }

  .schedule { left: 49px; top: 772px; display: flex; gap: 39px; }
  .date-card {
    width: 176px; height: 208px; border-radius: 8px; overflow: hidden;
    background: var(--card);
    box-shadow: 0 5px 0 var(--card-edge), 0 8px 12px rgba(0,0,0,.18);
    text-align: center; position: relative;
  }
  .date-card-head {
    height: 74px; background: linear-gradient(180deg, var(--red-dark) 0 8px, var(--red) 8px);
    color: var(--paper); font-size: 24px; padding-top: 32px; position: relative;
  }
  .date-card-head::before, .date-card-head::after {
    content: ""; position: absolute; top: 18px; width: 13px; height: 13px; border-radius: 50%;
    background: radial-gradient(circle, #9a9a9a 35%, #e6e6e6 40%, #7a7a7a 100%);
  }
  .date-card-head::before { left: 13px; }
  .date-card-head::after { right: 13px; }
  .date-day {
    font-family: "Anton", sans-serif; font-size: 44px; line-height: 1; margin-top: 12px; color: var(--navy);
  }
  .date-day sup { font-size: 24px; vertical-align: 18px; }
  .date-weekday { font-size: 17px; margin-top: 8px; color: var(--navy); }
  .date-time { font-family: "Anton", sans-serif; font-size: 21px; margin-top: 4px; color: var(--navy); }

  .contact {
    left: 0; width: 927px; text-align: center;
    font-family: "Anton", sans-serif; color: var(--navy); line-height: 1; white-space: nowrap;
  }
  .contact-line-1 { top: 1075px; font-size: 27px; }
  .contact-line-2 { top: 1111px; font-size: 27px; letter-spacing: 1.1px; }
</style>
</head>
<body>
  <h1 class="abs event-title">KESTREL</h1>
  <div class="abs event-subtitle">Summit</div>
  <div class="abs event-year">2020</div>
  <div class="abs dove dove-top" role="img" aria-label="White dove in flight"></div>

  <div class="abs brand">
    <span class="brand-dot"></span>
    <span class="brand-name">ORVEN</span>
  </div>

  <div class="abs speaker-photo" role="img" aria-label="Photo of the speaker, Prophet Marcus Olunde"></div>

  <p class="abs theme">
    <span class="theme-line">“IN FIRE</span>
    <span class="theme-line theme-line-2">ON FIRE”</span>
  </p>
  <div class="abs theme-amp">&amp;</div>

  <p class="abs focus-words">FIRE &nbsp;| &nbsp;REVIVAL &nbsp;| &nbsp;PROPHETIC</p>

  <div class="abs dove dove-mid" role="img" aria-label="White dove in flight"></div>

  <p class="abs speaker">SPEAKER: PROPHET MARCUS OLUNDE</p>

  <div class="abs schedule">
    <div class="date-card">
      <div class="date-card-head">December</div>
      <div class="date-day">31<sup>st</sup></div>
      <div class="date-weekday">Thursday</div>
      <div class="date-time">6:30PM</div>
    </div>
    <div class="date-card">
      <div class="date-card-head">January</div>
      <div class="date-day">01<sup>st</sup></div>
      <div class="date-weekday">Friday</div>
      <div class="date-time">6:30PM</div>
    </div>
    <div class="date-card">
      <div class="date-card-head">January</div>
      <div class="date-day">02<sup>nd</sup></div>
      <div class="date-weekday">Saturday</div>
      <div class="date-time">6:30PM</div>
    </div>
    <div class="date-card">
      <div class="date-card-head">January</div>
      <div class="date-day">03<sup>rd</sup></div>
      <div class="date-weekday">Sunday</div>
      <div class="date-time">4:30PM</div>
    </div>
  </div>

  <p class="abs contact contact-line-1">CONTACT@BRIGHTMEADOWFOLD.ORG, TELEPHONE NUMBER: 207 583 2914</p>
  <p class="abs contact contact-line-2">HARLOW COMMUNITY CENTER, 239 FENNIMORE STREET, PORTLAND, ME 04117</p>
</body>
</html>
```